Cadenza Elite Keyboard Academy is a comprehensive piano studio located in CBD area and provide individual piano lessons.

We also provide services for wedding organising band, or instrumental hiring or venue hiring, or organise concert to students.

I want my name card to be very creative, does not have to be the form or shape with the normal name card, can be in different shape. Also, I want the name card to be very upper class, because learning piano is a serious thing, so I do not want people to bargain with the prices. I want people to see it as a very elegant tuition so that they do not want to bargain and think it is worth to try.

Further more, Cadenza Elite Keyboard Academy is not like normal piano studio only provide piano lessons, we provide band services for each other event, such as cruise party, wedding etc. I want people to see it as owner of Elite Keyboard Academy, they will have different type of services all in one, I provide more than that, and I am well connected. I do not provide only piano lesson, but also all other musical knowledge and I am very professional

I want name card to be very simple, just name of company name, my name and website that's all, maybe phone number and email as well.

Please check my website to have more ideal concept.
http://harrietdowse.sitebuilder-example.com/cadenzakeyboard
Updates

Target Market(s)

For all people who love to play piano (better with upper class)

Industry/Entity Type

Wedding

Contact Information for Business Card

Harriet Dowse
Mobile:0418769052
Email: cadenzaelitekeys@mailbox-example.com

Colors

Designer to choose colors to be used in the design.

Requirements
Must have
• Creativity
Nice to have
• Black and white
some sort of piano image
Should not have
• Childish

```html
<!DOCTYPE html>
<html lang="en">
<head>
<meta charset="utf-8">
<title>Cadenza Elite Keyboard Academy – Business Card</title>
<link rel="stylesheet" href="https://fonts.googleapis.com/css2?family=Josefin+Sans:wght@300;400&family=Playfair+Display:wght@400&display=swap">
<style>
  :root{
    --backdrop:#e9e9e9;
    --card-black:#050505;
    --card-white:#ffffff;
    --ink-white:#ffffff;
    --ink-dark:#141414;
    --contact-blue:#3b3f9c;
    --staff-grey:#dcdcdc;
    --clef-grey:#ececec;
    --keys-light:#f4f4f4;
    --keys-mid:#b9b9b9;
  }
  *{box-sizing:border-box;margin:0;padding:0}
  html,body{width:1200px;height:900px;overflow:hidden}
  body{background:var(--backdrop);position:relative;font-family:"Josefin Sans",sans-serif}

  .card{position:absolute;box-shadow:4px 5px 6px rgba(0,0,0,.35)}

  /* front */
  .card-front{left:57px;top:55px;width:608px;height:320px;background:var(--card-black);border-top-right-radius:95px;overflow:hidden}
  .keys-area{position:absolute;left:0;top:0;width:210px;height:100%;
    background:linear-gradient(180deg,var(--keys-light) 0%,var(--keys-mid) 50%,var(--keys-light) 100%)}
  .brand{position:absolute;left:300px;top:30px;color:var(--ink-white);font-weight:300;line-height:1.05}
  .brand span{display:block}
  .brand .line-1{font-size:40px;margin-left:12px}
  .brand .line-2{font-size:36px;margin-top:6px}
  .brand .line-3{font-size:40px;margin-top:8px;margin-left:60px}
  .dots{position:absolute;left:428px;top:246px;color:var(--ink-white);font-size:14px;letter-spacing:3px}
  .tagline{position:absolute;left:265px;top:268px;width:330px;color:var(--ink-white);
    font-family:"Playfair Display",serif;font-size:19px;line-height:1.35}

  /* back */
  .card-back{left:423px;top:425px;width:617px;height:322px;background:var(--card-white);border-top-left-radius:95px;overflow:hidden}
  .staff{position:absolute;left:0;top:58px;width:100%;height:92px}
  .clef-area{position:absolute;left:50px;top:48px;width:34px;height:112px;background:var(--clef-grey);border-radius:17px}
  .person-name{position:absolute;left:158px;top:78px;font-size:60px;font-weight:300;color:var(--ink-dark);letter-spacing:1px}
  .contact{position:absolute;display:flex;align-items:center;gap:9px;color:var(--contact-blue);font-size:17px;font-weight:300}
  .contact svg{flex:none}
  .contact-phone{left:40px;top:207px}
  .contact-email{left:245px;top:207px}
  .contact-web{left:100px;top:258px}
</style>
</head>
<body>

<section class="card card-front" aria-label="Business card front">
  <div class="keys-area" role="img" aria-label="Piano keyboard keys seen from above"></div>
  <h1 class="brand">
    <span class="line-1">Cadenza</span>
    <span class="line-2">Elite Keyboard</span>
    <span class="line-3">Academy</span>
  </h1>
  <div class="dots">••••</div>
  <p class="tagline">Unique premium comprehensive tuition in Sydney.</p>
</section>

<section class="card card-back" aria-label="Business card back">
  <svg class="staff" viewBox="0 0 617 92" preserveAspectRatio="none" aria-hidden="true">
    <g stroke="var(--staff-grey)" stroke-width="1.5">
      <line x1="0" y1="2" x2="617" y2="2"/>
      <line x1="0" y1="24" x2="617" y2="24"/>
      <line x1="0" y1="46" x2="617" y2="46"/>
      <line x1="0" y1="68" x2="617" y2="68"/>
      <line x1="0" y1="90" x2="617" y2="90"/>
    </g>
  </svg>
  <div class="clef-area" role="img" aria-label="Faint treble clef"></div>
  <h2 class="person-name">Harriet Dowse</h2>

  <div class="contact contact-phone">
    <svg width="14" height="22" viewBox="0 0 14 22" aria-hidden="true">
      <rect x="1" y="3" width="12" height="18" rx="2" fill="none" stroke="currentColor" stroke-width="1.6"/>
      <line x1="3" y1="0" x2="3" y2="3" stroke="currentColor" stroke-width="1.6"/>
      <rect x="3.5" y="6" width="7" height="5" fill="currentColor"/>
      <g fill="currentColor"><circle cx="4.5" cy="14" r="1"/><circle cx="7" cy="14" r="1"/><circle cx="9.5" cy="14" r="1"/><circle cx="4.5" cy="17" r="1"/><circle cx="7" cy="17" r="1"/><circle cx="9.5" cy="17" r="1"/></g>
    </svg>
    <span>0418 769 052</span>
  </div>

  <div class="contact contact-email">
    <svg width="20" height="16" viewBox="0 0 20 16" aria-hidden="true">
      <path d="M1 7 L10 1 L19 7 V15 H1 Z" fill="none" stroke="currentColor" stroke-width="1.6"/>
      <path d="M1 7 L10 12 L19 7" fill="none" stroke="currentColor" stroke-width="1.6"/>
    </svg>
    <span>cadenzaelitekeys@mailbox-example.com</span>
  </div>

  <div class="contact contact-web">
    <svg width="19" height="19" viewBox="0 0 20 20" aria-hidden="true">
      <g fill="none" stroke="currentColor" stroke-width="1.5">
        <circle cx="10" cy="10" r="8.5"/>
        <ellipse cx="10" cy="10" rx="3.8" ry="8.5"/>
        <line x1="1.5" y1="10" x2="18.5" y2="10"/>
        <path d="M3 5.5 H17 M3 14.5 H17"/>
      </g>
    </svg>
    <span>harrietdowse.sitebuilder-example.com/cadenzakeyboard</span>
  </div>
</section>

</body>
</html>
```